Book Cover

Hello!
I need someone to design a book cover with the title, subtitle and one of the photos attached.

- Title: Weathering Tidewater - By Corwin Hadley
- Subtitle: A Steady Handbook for building a calm and joyful path after the news.

```html
<!DOCTYPE html>
<html lang="en">
<head>
<meta charset="utf-8">
<title>Weathering Tidewater – Book Cover</title>
<link href="https://fonts.googleapis.com/css2?family=Archivo+Black&family=Montserrat:wght@500;800&display=swap" rel="stylesheet">
<style>
  :root {
    --backdrop: #e6e4e8;
    --paper: #f4f4f2;
    --ink-blue: #2f5fc0;
    --band-blue: #2c5cc0;
    --art-light: #e4e4e4;
    --art-mid: #c9cdd6;
    --art-deep: #8e9bb8;
    --white: #ffffff;
  }
  * { margin: 0; padding: 0; box-sizing: border-box; }
  html, body {
    width: 1200px;
    height: 923px;
    overflow: hidden;
    background: var(--backdrop);
  }
  .stage {
    width: 1200px;
    height: 923px;
    display: flex;
    align-items: center;
    justify-content: center;
  }
  .cover {
    position: relative;
    width: 530px;
    height: 880px;
    background: var(--paper);
    box-shadow: 0 10px 30px rgba(0,0,0,0.12);
    overflow: hidden;
  }
  .cover-title {
    position: absolute;
    top: 100px;
    left: 0;
    right: 0;
    text-align: center;
    font-family: "Archivo Black", sans-serif;
    color: var(--ink-blue);
    line-height: 0.98;
    text-transform: uppercase;
    font-weight: 400;
  }
  .cover-title .line-one { display: block; font-size: 54px; letter-spacing: -1px; }
  .cover-title .line-two { display: block; font-size: 66px; letter-spacing: -1.5px; }
  .cover-subtitle {
    position: absolute;
    top: 248px;
    left: 110px;
    right: 110px;
    text-align: center;
    font-family: "Montserrat", sans-serif;
    font-weight: 500;
    font-size: 9px;
    letter-spacing: 1.2px;
    line-height: 1.5;
    color: var(--ink-blue);
    text-transform: uppercase;
  }
  .cover-art {
    position: absolute;
    top: 310px;
    left: 150px;
    width: 230px;
    height: 430px;
    background: linear-gradient(180deg, var(--art-light) 0%, var(--art-mid) 55%, var(--art-deep) 100%);
  }
  .author-band {
    position: absolute;
    left: 0;
    right: 0;
    bottom: 0;
    height: 96px;
    background: var(--band-blue);
    display: flex;
    flex-direction: column;
    align-items: center;
    justify-content: center;
    color: var(--white);
    text-transform: uppercase;
  }
  .author-band .by {
    font-family: "Montserrat", sans-serif;
    font-weight: 800;
    font-size: 9px;
    letter-spacing: 2px;
    margin-bottom: 4px;
  }
  .author-band .author-name {
    font-family: "Archivo Black", sans-serif;
    font-size: 34px;
    letter-spacing: 2px;
    line-height: 1;
  }
</style>
</head>
<body>
<main class="stage">
  <article class="cover">
    <h1 class="cover-title">
      <span class="line-one">Weathering</span>
      <span class="line-two">Tidewater</span>
    </h1>
    <p class="cover-subtitle">A Steady Handbook for building a calm and joyful path after the news.</p>

    <div class="cover-art" role="img" aria-label="Hourglass illustration framing two photos of the author, one black-and-white above and one in colour below"></div>

    <footer class="author-band">
      <span class="by">By</span>
      <span class="author-name">Corwin Hadley</span>
    </footer>
  </article>
</main>
</body>
</html>
```